WTF!!! We need a modern professional website for a business litigation law firm.

We need a modern, clean, professional and uncomplicated website for a new business trial and litigation law firm called "Hallorand Trial Firm PLLC". Website must be mobile optimized for iPad and smartphone. The law firm specializes in counseling and representing large corporations, small businesses and entrepreneurs in and out of the courtroom. Lawyers in the firm serve as Florida counsel and trial counsel to organizations facing claims involving product liability, premises liability, professional liability, vehicle and transportation liability, warranty claims, construction defects and delay claims, complex business disputes, commercial litigation and bid disputes in State and Federal Courts. The website is mainly to provide information about the firm, and should include sections describing the firm, identifying the Industries Served and Areas of Practice ," a separate page identifying the "Professionals", a separate page for "Resources & Advisories," and a traveling "Connect With Us" button a site visitor can click on that will launch an email to the Firm's general email account. The website should allow us to easily modify the content on these pages, and let us add/modify links to external information sources. We will not sell anything or take payments through the website. We do need to be able to easily upload and update photographs of attorneys and add new attorneys names/email hyperlinks as the firm grows. We would like to add developments in the law or success stories easily and quickly, such as through a blog page. On the "Connect With Us" page the website should have hyperlinks to email the Firm, and there should be hyperlinks to email each professional on the "Professionals" page. The website should be viewable on mobile devices without distortion. The law firm focuses on trial work and should have some imagery associated with courtrooms, but the overall theme of the site should be modern, clean, and communicate sophistication and strength. The website should be made in Wordpress. We have uploaded logo files for Hallorand Trial Firm.

Target Market(s)

Corporations and companies that are looking for legal representation. Other attorneys/legal industry.

Industry/Entity Type

Legal Industry

Coding

Coded - Design and coding required

Number of Pages Required

1 page

Font styles to use
Sans Serif

Requirements
Must have
• Simple, clean, sophisticated, modern website that includes the logo, watermark of logo, and the elements described above.
Nice to have
• Pictures of city scape, buildings, courtroom, team members.

```html
<!DOCTYPE html>
<html lang="en">
<head>
<meta charset="utf-8">
<title>Hallorand Trial Firm — Business Litigation</title>
<link rel="stylesheet" href="https://fonts.googleapis.com/css2?family=Montserrat:wght@400;500;600;700;800&family=Libre+Baskerville:wght@400;700&display=swap">
<style>
:root{
  --blue:#1e88e5;
  --gold:#c8925a;
  --gold-soft:#e9d6c0;
  --ink:#111111;
  --text:#555555;
  --muted:#9a9a9a;
  --grey-bg:#f1f1f1;
  --line:#dcdcdc;
  --white:#ffffff;
  --black:#0c0c0c;
}
*{box-sizing:border-box;margin:0;padding:0}
html,body{width:1200px;height:4854px;overflow:hidden}
body{font-family:"Montserrat",sans-serif;color:var(--text);background:var(--white);position:relative}
.abs{position:absolute}
.serif{font-family:"Libre Baskerville",serif}
.brand{font-family:"Montserrat",sans-serif;font-weight:800;color:var(--ink);letter-spacing:.5px;display:flex;align-items:center;gap:8px}
.brand .mark{width:22px;height:22px;background:var(--ink)}
.btn-gold{background:var(--gold);color:#fff;border-radius:20px;font-weight:600;font-size:12px;display:flex;align-items:center;justify-content:center}

/* header */
.site-header{position:absolute;left:0;top:0;width:1200px;height:155px;background:#fff}
.site-header .brand{left:141px;top:30px;font-size:20px;line-height:1.05}
.contact-chip{display:flex;align-items:center;gap:14px;font-size:12px;color:var(--ink)}
.contact-chip .ico{width:34px;height:34px;border:1px solid var(--line);display:flex;align-items:center;justify-content:center}
.contact-chip b{display:block;font-weight:600;font-size:11px}
.connect-btn{left:897px;top:30px;width:162px;height:40px;background:var(--blue);color:#fff;font-size:11px;font-weight:600;letter-spacing:.8px;display:flex;align-items:center;justify-content:center;border-bottom:3px solid #0b5db0}
.main-nav{left:141px;top:107px;width:918px;border-top:1px solid #e7e7e7;height:48px}
.main-nav a{position:absolute;top:16px;font-size:11.5px;font-weight:600;color:var(--ink);text-decoration:none;letter-spacing:.3px}
.main-nav a.active{color:var(--blue);border-bottom:2px solid var(--blue);padding-bottom:6px}

/* hero */
.hero{position:absolute;left:0;top:155px;width:1200px;height:540px;overflow:hidden}
.hero-photo{position:absolute;inset:0;background:linear-gradient(120deg,#0f2236 0%,#2b4a6b 35%,#6e8aa6 55%,#4b3b2a 80%,#1a150f 100%)}
.hero h1{position:absolute;left:141px;top:105px;font-size:40px;line-height:50px;font-weight:800;color:#fff;letter-spacing:.5px}
.hero p{position:absolute;left:143px;top:268px;font-size:18px;color:#fff}
.hero .learn{position:absolute;left:141px;top:320px;width:140px;height:45px;background:var(--blue);color:#fff;font-size:12px;font-weight:600;letter-spacing:.8px;display:flex;align-items:center;justify-content:center}
.hero-curve{position:absolute;left:0;top:440px}
.scroll-cue{left:557px;top:688px;width:76px;height:76px;border-radius:50%;background:#fff;box-shadow:0 4px 14px rgba(0,0,0,.15);display:flex;align-items:center;justify-content:center}

/* section headings */
.sec-title{position:absolute;left:0;width:1200px;text-align:center;font-family:"Libre Baskerville",serif;font-size:36px;font-weight:700;color:var(--ink)}
.sec-title span{color:var(--gold)}
.divider{position:absolute;left:540px;width:120px;height:14px}
.divider::before,.divider::after{content:"";position:absolute;top:6px;width:36px;height:1px;background:#999}
.divider::before{left:0}.divider::after{right:0}
.divider i{position:absolute;left:53px;top:0;width:14px;height:14px;background:var(--ink)}
.sec-lead{position:absolute;left:290px;width:620px;text-align:center;font-size:12.5px;line-height:22px;color:#444}
.arrow{width:28px;height:28px;border-radius:50%;display:flex;align-items:center;justify-content:center;font-size:14px}
.arrow.left{border:1px solid var(--gold);color:var(--gold);background:transparent}
.arrow.right{background:var(--gold);color:#fff}

/* about */
.about h2{left:141px;top:838px;font-family:"Libre Baskerville",serif;font-size:36px;color:var(--ink);font-weight:700}
.about h2 span{color:var(--gold)}
.about .small-rule{left:141px;top:893px;width:24px;height:12px;background:var(--ink)}
.about .intro{left:141px;top:925px;width:420px;font-size:12.5px;font-weight:600;color:var(--ink);line-height:23px}
.about .body{left:141px;width:425px;font-size:12.5px;line-height:22.5px;color:#555}
.about .more{left:141px;top:1222px;width:128px;height:38px}
.ph{position:absolute}

/* areas */
.band-grey{position:absolute;left:0;width:1200px;background:var(--grey-bg)}
.practice-card{position:absolute;top:1586px;width:287px;height:194px;background:#fff;padding:30px 24px}
.practice-card h3{font-family:"Libre Baskerville",serif;font-size:12px;color:var(--ink);font-weight:700}
.practice-card p{margin-top:46px;font-size:12px;line-height:19px;color:#666;width:200px}
.practice-card svg{position:absolute;right:24px;top:22px}

/* industries */
.industry{position:absolute;width:320px}
.industry h4{font-family:"Libre Baskerville",serif;font-size:12px;color:var(--ink);font-weight:700;margin-bottom:8px}
.industry p{font-size:12px;line-height:20px;color:#555}
.industry.r{text-align:right}
.industry.c{text-align:center}
.ind-icon{position:absolute;width:56px;height:56px;border-radius:50%;background:#fff;box-shadow:0 3px 12px rgba(0,0,0,.1);display:flex;align-items:center;justify-content:center}

/* testimonials */
.testimonial{position:absolute;top:2928px;width:443px;height:232px;background:#fff;padding:30px 28px}
.testimonial .avatar{position:absolute;left:28px;top:30px;width:66px;height:66px;border-radius:50%}
.testimonial .who{position:absolute;left:114px;top:50px}
.testimonial .who b{font-family:"Libre Baskerville",serif;font-size:13px;color:var(--ink)}
.testimonial .who small{display:block;font-size:11.5px;color:#666;margin-top:4px}
.testimonial .qmark{position:absolute;right:40px;top:10px;font-family:"Libre Baskerville",serif;font-size:110px;color:#e3e3e3;line-height:1}
.testimonial blockquote{position:absolute;left:28px;top:122px;width:380px;font-size:12px;font-style:italic;line-height:22.5px;color:#555;text-align:justify}
.dots{position:absolute;top:3194px;left:570px;display:flex;gap:5px;align-items:center}
.dots i{width:7px;height:7px;border-radius:50%;background:#ccc}
.dots i.on{width:10px;height:10px;background:var(--gold)}

/* resources */
.post{position:absolute;top:3531px;width:287px}
.post .thumb{height:228px}
.post .caption{position:relative;margin:-47px 22px 0;background:#fff;box-shadow:0 4px 14px rgba(0,0,0,.08);padding:20px 10px 16px;text-align:center}
.post .date{font-size:11px;color:#444}
.post h5{font-family:"Libre Baskerville",serif;font-size:12px;line-height:22px;color:var(--ink);margin-top:8px}
.post a{display:inline-block;margin-top:10px;font-size:11px;font-weight:600;color:var(--gold);text-decoration:underline}

/* contact */
.contact-card{position:absolute;left:141px;top:4009px;width:918px;height:569px;background:#fff;box-shadow:0 0 20px rgba(0,0,0,.06)}
.field{position:absolute;width:318px;border-bottom:1px solid #bbb;font-size:11px;color:#888;padding:0 10px 8px}
.field.filled{color:var(--ink);border-bottom:2px solid #333}

/* footer */
.site-footer{position:absolute;left:0;top:4418px;width:1200px;height:436px;background:var(--black);color:#ddd}
.site-footer .brand{color:#fff}
.site-footer .brand .mark{background:#fff}
.f-col{position:absolute;top:217px}
.f-col h6{font-family:"Libre Baskerville",serif;font-size:12px;color:#fff;font-weight:700;margin-bottom:16px}
.f-col li{list-style:none;font-size:11px;color:#fff;margin-bottom:11px}
.f-col li::before{content:"•";margin-right:8px}
.f-contact{display:flex;gap:14px;font-size:11px;color:#fff;margin-bottom:14px;line-height:19px}
.socials{position:absolute;right:141px;top:398px;display:flex;gap:8px}
.socials i{width:17px;height:17px;border-radius:50%;border:1px solid #aaa;display:block}
</style>
</head>
<body>

<!-- Header -->
<header class="site-header">
  <div class="abs brand"><span class="mark"></span><span>HALLORAND</span></div>
  <div class="abs contact-chip" style="left:446px;top:32px">
    <div class="ico"><svg width="14" height="14" viewBox="0 0 24 24"><path d="M6 2l4 4-2 3a12 12 0 0 0 7 7l3-2 4 4-3 4C10 22 2 14 2 5z" fill="#222"/></svg></div>
    <div><b>PHONE</b>123-456-7890</div>
  </div>
  <div class="abs contact-chip" style="left:616px;top:32px">
    <div class="ico"><svg width="15" height="12" viewBox="0 0 24 18"><rect x="1" y="1" width="22" height="16" fill="none" stroke="#222" stroke-width="2"/><path d="M1 1l11 9 11-9" fill="none" stroke="#222" stroke-width="2"/></svg></div>
    <div><b>EMAIL</b>info@hallorandtrialfirm.com</div>
  </div>
  <a class="abs connect-btn">CONNECT WITH US</a>
  <nav class="abs main-nav">
    <a class="active" style="left:22px">HOME</a>
    <a style="left:108px">ABOUT US</a>
    <a style="left:222px">PROFESSIONALS</a>
    <a style="left:376px">INDUSTRIES SERVED</a>
    <a style="left:552px">AREAS OF PRACTICE</a>
    <a style="left:730px">RESOURCES &amp; ADVISORIES</a>
  </nav>
</header>

<!-- Hero -->
<section class="hero">
  <div class="hero-photo" role="img" aria-label="Photo looking up at glass office towers against a cloudy sky"></div>
  <h1>YOUR TRUSTED<br>PARTNER IN BUSINESS<br>LITIGATION</h1>
  <p>Expert Counsel for Corporations and Entrepreneurs.</p>
  <a class="learn">LEARN MORE</a>
  <svg class="hero-curve" width="1200" height="100" viewBox="0 0 1200 100">
    <path d="M0 55 Q600 135 1200 0 L1200 100 L0 100Z" fill="#1e88e5"/>
    <path d="M0 78 Q600 150 1200 30 L1200 100 L0 100Z" fill="#fff"/>
  </svg>
</section>
<div class="abs scroll-cue">
  <svg width="22" height="32" viewBox="0 0 22 32"><rect x="1.5" y="1.5" width="19" height="29" rx="9.5" fill="none" stroke="#1e88e5" stroke-width="2"/><path d="M7 13l4 4 4-4M7 18l4 4 4-4" fill="none" stroke="#1e88e5" stroke-width="1.6"/></svg>
</div>

<!-- About -->
<section class="about">
  <h2 class="abs">About <span>Hallorand</span></h2>
  <div class="abs small-rule"></div>
  <p class="abs intro">Lorem Ipsum Dolor Sit Amet, Consectetur Adipiscing Elit.<br>Donec Consequat Finibus Augue</p>
  <p class="abs body" style="top:982px">Cras Eu Est Molestie, Vehicula Ipsum Scelerisque, Mattis Lorem. Quisque Sodales Gravida Diam. Suspendisse Nulla Dolor, Placerat Id Tempus Vitae, Ultricies Eget Nisl.</p>
  <p class="abs body" style="top:1057px">Vivamus Vestibulum Dolor Eu Massa Blandit Luctus. Sed Molestie, Leo Eget Placerat Mollis, Leo Tortor Tristique Eros, Eu Sollicitudin Ligula Odio Non Enim. Pellentesque Mollis Magna Odio, In Condimentum Dui Feugiat Eleifend. Praesent Eget Neque Nec Mi Finibus Finibus. Aliquam Nec Porta Justo, Sed Accumsan Urna. Nam Non Est Elit.</p>
  <a class="abs btn-gold more">Learn More</a>
  <div class="ph" role="img" aria-label="Attorney in a suit reading documents" style="left:607px;top:870px;width:255px;height:148px;background:linear-gradient(135deg,#d9d9d9,#6b6f75)"></div>
  <div class="ph" role="img" aria-label="Hand signing a contract" style="left:873px;top:910px;width:113px;height:108px;background:linear-gradient(135deg,#efe6dc,#9d8a74)"></div>
  <div class="ph" role="img" aria-label="Team of three lawyers standing outside an office" style="left:643px;top:1030px;width:150px;height:212px;background:linear-gradient(180deg,#8ea0b5,#3b4656)"></div>
  <div class="ph" role="img" aria-label="Documents and a cup of coffee on a dark desk" style="left:803px;top:1030px;width:256px;height:148px;background:linear-gradient(135deg,#2d241b,#7a5d3d)"></div>
  <div class="ph" role="img" aria-label="Faint line drawing of scales of justice" style="left:880px;top:1205px;width:160px;height:142px;background:radial-gradient(circle,#f3e7da 0%,#fff 70%)"></div>
</section>

<!-- Areas of practice -->
<div class="band-grey" style="top:1347px;height:613px"></div>
<h2 class="sec-title" style="top:1420px">Areas Of <span>Practice</span></h2>
<div class="divider" style="top:1473px"><i></i></div>
<p class="sec-lead" style="top:1504px">Cras Eu Est Molestie, Vehicula Ipsum Scelerisque, Mattis Lorem. Quisque Sodales Gravida Diam. Suspendisse Nulla Dolor, Placerat Id Tempus Vitae, Ultricies Eget Nisl.</p>
<div class="abs arrow left" style="left:77px;top:1670px">‹</div>
<div class="abs arrow right" style="left:1095px;top:1670px">›</div>
<article class="practice-card" style="left:141px">
  <h3>Product Liability</h3>
  <svg width="30" height="34" viewBox="0 0 30 34" fill="none" stroke="#c8925a" stroke-width="1.6"><rect x="4" y="2" width="22" height="30"/><path d="M9 10h12M9 16h12M9 22h8"/></svg>
  <p>It is a long established fact that a reader will be distracted by the readable content of a page when looking.</p>
</article>
<article class="practice-card" style="left:456px">
  <h3>Remises Liability</h3>
  <svg width="34" height="34" viewBox="0 0 34 34" fill="none" stroke="#c8925a" stroke-width="1.6"><rect x="3" y="6" width="20" height="24"/><circle cx="24" cy="20" r="8"/><path d="M7 12h12M7 18h8"/></svg>
  <p>It is a long established fact that a reader will be distracted by the readable content of a page when looking.</p>
</article>
<div class="abs arrow right" style="left:482px;top:1768px;width:32px;height:32px">→</div>
<article class="practice-card" style="left:772px">
  <h3>Professional Liability</h3>
  <svg width="32" height="34" viewBox="0 0 32 34" fill="none" stroke="#c8925a" stroke-width="1.6"><circle cx="16" cy="12" r="8"/><path d="M4 32c2-8 22-8 24 0M16 8v8M12 12h8"/></svg>
  <p>It is a long established fact that a reader will be distracted by the readable content of a page when looking.</p>
</article>
<a class="abs btn-gold" style="left:548px;top:1836px;width:104px;height:38px">View All</a>

<!-- Industries served -->
<h2 class="sec-title" style="top:2034px">Industries We <span>Served</span></h2>
<div class="divider" style="top:2086px"><i></i></div>
<p class="sec-lead" style="top:2117px">Cras Eu Est Molestie, Vehicula Ipsum Scelerisque, Mattis Lorem. Quisque Sodales Gravida Diam. Suspendisse Nulla Dolor, Placerat Id Tempus Vitae, Ultricies Eget Nisl.</p>
<svg class="abs" style="left:420px;top:2138px" width="340" height="340" viewBox="0 0 340 340"><circle cx="170" cy="170" r="160" fill="none" stroke="#d8b893" stroke-width="1.2" stroke-dasharray="6 6"/></svg>
<div class="abs" style="left:483px;top:2201px;width:214px;height:214px;border-radius:50%;background:#fff;box-shadow:0 6px 24px rgba(0,0,0,.08);display:flex;align-items:center;justify-content:center">
  <div class="brand" style="font-size:22px"><span class="mark"></span><span>HALLORAND</span></div>
</div>
<div class="industry r" style="left:76px;top:2196px"><h4>Large Corporations</h4><p>It is a long established fact that a reader will be distracted by the readable content of a page when looking.</p></div>
<div class="industry" style="left:786px;top:2196px"><h4>Transportation &amp; Logistics</h4><p>It is a long established fact that a reader will be distracted by the readable content of a page when looking.</p></div>
<div class="industry r" style="left:81px;top:2360px"><h4>Small Businesses</h4><p>It is a long established fact that a reader will be distracted by the readable content of a page when looking.</p></div>
<div class="industry" style="left:771px;top:2360px"><h4>Construction &amp; Real Estate</h4><p>It is a long established fact that a reader will be distracted by the readable content of a page when looking.</p></div>
<div class="industry c" style="left:430px;top:2526px"><h4>Entrepreneurs &amp; Startups</h4><p>It is a long established fact that a reader will be distracted by the readable content of a page when looking.</p></div>
<div class="ind-icon" style="left:420px;top:2208px"><svg width="26" height="26" viewBox="0 0 26 26" fill="none" stroke="#c8925a" stroke-width="1.5"><path d="M3 24h20M5 24V10h16v14M3 10l10-7 10 7M9 14v6M13 14v6M17 14v6"/></svg></div>
<div class="ind-icon" style="left:705px;top:2208px"><svg width="28" height="24" viewBox="0 0 28 24" fill="none" stroke="#c8925a" stroke-width="1.5"><path d="M2 6h15v12H2zM17 10h5l4 4v4h-9"/><circle cx="7" cy="20" r="2.5"/><circle cx="21" cy="20" r="2.5"/></svg></div>
<div class="ind-icon" style="left:426px;top:2370px"><svg width="22" height="26" viewBox="0 0 22 26" fill="none" stroke="#c8925a" stroke-width="1.5"><path d="M3 8h16v16H3zM3 8l3-6h10l3 6M8 24v-7h6v7"/></svg></div>
<div class="ind-icon" style="left:690px;top:2370px"><svg width="26" height="26" viewBox="0 0 26 26" fill="none" stroke="#c8925a" stroke-width="1.5"><path d="M2 24h22M4 24V8h8v16M12 24V3h10v21M7 12h2M7 16h2M15 8h4M15 12h4M15 16h4"/></svg></div>
<div class="ind-icon" style="left:562px;top:2449px"><svg width="26" height="26" viewBox="0 0 26 26" fill="none" stroke="#c8925a" stroke-width="1.5"><circle cx="13" cy="13" r="5"/><path d="M13 2v5M13 19v5M2 13h5M19 13h5M5 5l3 3M18 18l3 3M21 5l-3 3M8 18l-3 3"/></svg></div>

<!-- Testimonials -->
<div class="band-grey" style="top:2685px;height:603px"></div>
<h2 class="sec-title" style="top:2764px">What Our <span>Clients Say</span></h2>
<div class="divider" style="top:2815px"><i></i></div>
<p class="sec-lead" style="top:2846px">Cras Eu Est Molestie, Vehicula Ipsum Scelerisque, Mattis Lorem. Quisque Sodales Gravida Diam. Suspendisse Nulla Dolor, Placerat Id Tempus Vitae, Ultricies Eget Nisl.</p>
<div class="abs arrow left" style="left:77px;top:3031px">‹</div>
<div class="abs arrow right" style="left:1095px;top:3031px">›</div>
<article class="testimonial" style="left:141px">
  <div class="avatar" role="img" aria-label="Portrait of client John Die" style="background:linear-gradient(135deg,#d8c2ae,#5a4a3e)"></div>
  <div class="who"><b>John Die</b><small>CEO At Lorem</small></div>
  <div class="qmark">”</div>
  <blockquote>" Suspendisse lobortis semper mi in hendrerit. Proin eros nisl, faucibus in suscipit at, rutrum vel metus. Mauris faucibus odio gravida bibendum dignissim. Nulla vitae finibus velit, in bibendum quam. "</blockquote>
</article>
<article class="testimonial" style="left:616px">
  <div class="avatar" role="img" aria-label="Portrait of client Ariadne" style="background:linear-gradient(135deg,#f1e2cf,#b89a78)"></div>
  <div class="who"><b>Ariadne</b><small>CEO At Lorem</small></div>
  <div class="qmark">”</div>
  <blockquote>" Suspendisse lobortis semper mi in hendrerit. Proin eros nisl, faucibus in suscipit at, rutrum vel metus. Mauris faucibus odio gravida bibendum dignissim. Nulla vitae finibus velit, in bibendum quam. "</blockquote>
</article>
<div class="dots"><i></i><i></i><i class="on"></i><i></i><i></i></div>

<!-- Resources -->
<h2 class="sec-title" style="top:3367px">Resources &amp; <span>Advisories</span></h2>
<div class="divider" style="top:3419px"><i></i></div>
<p class="sec-lead" style="top:3450px">Cras Eu Est Molestie, Vehicula Ipsum Scelerisque, Mattis Lorem. Quisque Sodales Gravida Diam. Suspendisse Nulla Dolor, Placerat Id Tempus Vitae, Ultricies Eget Nisl.</p>
<div class="abs arrow left" style="left:77px;top:3680px">‹</div>
<div class="abs arrow right" style="left:1095px;top:3680px">›</div>
<article class="post" style="left:141px">
  <div class="thumb" role="img" aria-label="Business people meeting in a bright office" style="background:linear-gradient(135deg,#f4f6f8,#8d99a6)"></div>
  <div class="caption"><div class="date">▭ 23 Jan2025</div><h5>Lorem Ipsum Dolor Sit Amet, Consectetur Adipiscing Elit...</h5><a>Read More</a></div>
</article>
<article class="post" style="left:456px">
  <div class="thumb" role="img" aria-label="Lawyer holding legal papers" style="background:linear-gradient(135deg,#3a2f26,#b39a7c)"></div>
  <div class="caption"><div class="date">▭ 23 Jan2025</div><h5>Lorem Ipsum Dolor Sit Amet, Consectetur Adipiscing Elit...</h5><a>Read More</a></div>
</article>
<article class="post" style="left:772px">
  <div class="thumb" role="img" aria-label="Statue of justice with gavel in a courtroom" style="background:linear-gradient(135deg,#1e1812,#8a6a45)"></div>
  <div class="caption"><div class="date">▭ 23 Jan2025</div><h5>Lorem Ipsum Dolor Sit Amet, Consectetur Adipiscing Elit...</h5><a>Read More</a></div>
</article>
<a class="abs btn-gold" style="left:548px;top:3888px;width:104px;height:38px">View All</a>

<!-- Footer band (behind contact card) -->
<footer class="site-footer">
  <div class="abs brand" style="left:141px;top:205px;font-size:18px"><span class="mark"></span><span>HALLORAND</span></div>
  <p class="abs" style="left:141px;top:275px;width:290px;font-size:11px;line-height:19px;color:#fff">Cras eu est molestie, vehicula ipsum scelerisque, mattis lorem. Quisque sodales gravida diam. Suspendisse nulla dolor, placerat id tempus vitae.</p>
  <div class="f-col" style="left:494px"><h6>Quick Links</h6><ul><li>Home</li><li>About Us</li><li>Areas of Practice</li><li>Our Professionals</li></ul></div>
  <div class="f-col" style="left:678px"><h6>Useful Links</h6><ul><li>Resources &amp; Advisories</li><li>Contact Us</li><li>Privacy Policy</li><li>Terms &amp; Conditions</li></ul></div>
  <div class="f-col" style="left:885px"><h6>Stay In Touch</h6>
    <div class="f-contact"><span>☏</span><b>+1 123 456 7890</b></div>
    <div class="f-contact"><span>✉</span>info@hallorand.ca</div>
    <div class="f-contact"><span>⌾</span>123, Building Name, Street,<br>City, State XY 123456</div>
  </div>
  <div class="abs" style="left:141px;top:370px;width:918px;height:1px;background:#333"></div>
  <p class="abs" style="left:141px;top:400px;font-size:11px;color:#fff">Copyright @2025 Hallorand. All Rights Reserved</p>
  <div class="socials"><i></i><i></i><i></i><i></i></div>
</footer>

<!-- Contact -->
<section class="contact-card">
  <h2 class="sec-title" style="left:0;width:918px;top:78px">Get In <span>Touch With Us</span></h2>
  <div class="divider" style="left:399px;top:132px"><i></i></div>
  <div class="field filled" style="left:116px;top:196px">Your First Name*</div>
  <div class="field" style="left:484px;top:196px">Your Last Name*</div>
  <div class="field" style="left:116px;top:266px">Enter Your Email Adress*</div>
  <div class="field" style="left:484px;top:266px">Your Phone Number*</div>
  <div class="field" style="left:116px;top:336px;width:686px;height:74px">Your Message</div>
  <a class="abs btn-gold" style="left:407px;top:445px;width:104px;height:38px">Submit</a>
</section>

</body>
</html>
```